Price Calculator as Responsive Web App to support Sales People

We need to build a simple micro web app to support sales people in making quotes. We already have a backend that can take a number of parameters and create a quote. We need put a responsive web app on top of this so that our people on the road can easily do their price simulations.

We need two pages. One for the input and another for the results. No menus, navigations, etc. It is 6 different inputs as shown with boxes in the sketch. They don't need to be boxed, but some of them have a bit of instruction text that clearly need to belong to the input.

This needs to be responsive, but first and foremost designed for smartphones. I have included a background gradient that we would like to use -- or a variant of it. We expect this to be delivered as HTML/CSS + images so that we can quickly write a few pieces of JavaScript ourselves to wire it up to our price simulator.

Industry/Entity Type

Information Technology

Coding

Coded - Design and coding required

Number of Pages Required

2 page

Font styles to use
Sans Serif

Requirements
Must have
• Responsive design
• Easy to wire up JavaScript to the HTML/CSS
Nice to have
• Some quick way to pick number of months. +/- buttons to add remove a year or 3 months. Same thing with number of items. Add 10 or 5 quickly.
• Maybe some parallax effect while scrolling as long as it is not distracting.
Should not have
• Toolbars, Menus, Navigations, Banners, etc. This is just a single micro app.

```html
<!DOCTYPE html>
<html lang="en">
<head>
<meta charset="utf-8">
<title>Price Calculator</title>
<link rel="stylesheet" href="https://fonts.googleapis.com/css2?family=Open+Sans:wght@400;600&display=swap">
<style>
  :root {
    --bg-deep: #03152a;
    --bg-mid: #0c3d66;
    --band-inputs: #cde5f8;
    --band-engine: #e3f1fb;
    --band-storage: #d3e8f8;
    --band-extras: #cfe6f9;
    --ink: #2b2b2b;
    --ink-soft: #444;
    --accent: #1a8fe3;
    --field: #ffffff;
    --field-line: #b9d3e8;
    --radio-line: #c4c9ce;
    --radio-top: #ffffff;
    --radio-bottom: #dcdfe2;
  }
  * { box-sizing: border-box; margin: 0; padding: 0; }
  html, body { width: 698px; height: 1200px; overflow: hidden; }
  body {
    font-family: "Open Sans", sans-serif;
    color: var(--ink);
    background: radial-gradient(ellipse at 50% 45%, var(--bg-mid) 0%, #072a4c 45%, var(--bg-deep) 100%);
    position: relative;
  }
  .calculator {
    position: absolute;
    left: 56px; top: 56px;
    width: 592px; height: 1104px;
  }
  .band { position: relative; width: 100%; }
  .band--inputs { height: 200px; background: var(--band-inputs); }
  .band--engine { height: 414px; background: var(--band-engine); }
  .band--storage { height: 160px; background: var(--band-storage); }
  .band--extras { height: 330px; background: var(--band-extras); }

  .abs { position: absolute; }
  .mid { transform: translateY(-50%); }

  .stepper-label { left: 24px; font-size: 28px; line-height: 40px; }
  .step-btn {
    width: 36px; height: 36px; border-radius: 50%;
    background: var(--accent); transform: translateY(-50%);
    display: block;
  }
  .field {
    width: 48px; height: 52px;
    background: var(--field);
    border: 1px solid var(--field-line);
    transform: translateY(-50%);
  }
  .unit { left: 366px; font-size: 20px; line-height: 30px; }

  .group-title { left: 24px; font-size: 27px; line-height: 40px; }
  .group-title small { font-size: 21px; }

  .radio {
    width: 28px; height: 28px; border-radius: 50%;
    border: 1px solid var(--radio-line);
    background: linear-gradient(var(--radio-top), var(--radio-bottom));
    transform: translateY(-50%);
  }
  .opt { font-size: 26px; line-height: 36px; }
  .note { left: 24px; width: 540px; font-size: 21px; line-height: 32px; color: var(--ink-soft); }
</style>
</head>
<body>
<main class="calculator">

  <section class="band band--inputs">
    <span class="abs mid stepper-label" style="top:64px">Duration</span>
    <svg class="abs step-btn" style="left:184px;top:64px" viewBox="0 0 36 36"><rect x="9" y="15.5" width="18" height="5" fill="#fff"/></svg>
    <div class="abs field" style="left:234px;top:64px"></div>
    <div class="abs field" style="left:302px;top:64px"></div>
    <span class="abs mid unit" style="top:66px">Months</span>
    <div class="abs field" style="left:472px;top:64px"></div>
    <svg class="abs step-btn" style="left:528px;top:64px" viewBox="0 0 36 36"><rect x="9" y="15.5" width="18" height="5" fill="#fff"/><rect x="15.5" y="9" width="5" height="18" fill="#fff"/></svg>

    <span class="abs mid stepper-label" style="top:136px">Count</span>
    <svg class="abs step-btn" style="left:184px;top:136px" viewBox="0 0 36 36"><rect x="9" y="15.5" width="18" height="5" fill="#fff"/></svg>
    <div class="abs field" style="left:234px;top:136px"></div>
    <div class="abs field" style="left:302px;top:136px"></div>
    <span class="abs mid unit" style="top:138px">Items</span>
    <div class="abs field" style="left:472px;top:136px"></div>
    <svg class="abs step-btn" style="left:528px;top:136px" viewBox="0 0 36 36"><rect x="9" y="15.5" width="18" height="5" fill="#fff"/><rect x="15.5" y="9" width="5" height="18" fill="#fff"/></svg>
  </section>

  <section class="band band--engine">
    <h2 class="abs mid group-title" style="top:38px;font-weight:400">Engine Power (<small>beyond standard</small>)</h2>

    <span class="abs radio" style="left:52px;top:122px"></span>
    <span class="abs mid opt" style="left:106px;top:122px">360 $</span>
    <span class="abs mid opt" style="left:220px;top:122px">year</span>
    <span class="abs mid opt" style="left:342px;top:122px">Bvonze power</span>

    <span class="abs radio" style="left:52px;top:174px"></span>
    <span class="abs mid opt" style="left:106px;top:174px">600 $</span>
    <span class="abs mid opt" style="left:220px;top:174px">year</span>
    <span class="abs mid opt" style="left:342px;top:174px">Silver power</span>

    <span class="abs radio" style="left:52px;top:224px"></span>
    <span class="abs mid opt" style="left:106px;top:224px">360 $</span>
    <span class="abs mid opt" style="left:220px;top:224px">year</span>
    <span class="abs mid opt" style="left:342px;top:224px">Gold power</span>

    <span class="abs radio" style="left:52px;top:276px"></span>
    <span class="abs mid opt" style="left:106px;top:276px">360 $</span>
    <span class="abs mid opt" style="left:220px;top:276px">year</span>
    <span class="abs mid opt" style="left:342px;top:276px">Bvonze power</span>

    <p class="abs note" style="top:328px">A basic engine lorem ipsum labal inclusivo pölser.</p>
  </section>

  <section class="band band--storage">
    <h2 class="abs mid group-title" style="top:44px;font-weight:400">Shared storage addition</h2>
    <span class="abs radio" style="left:52px;top:106px"></span>
    <span class="abs mid opt" style="left:96px;top:106px">10kg</span>
    <span class="abs radio" style="left:184px;top:106px"></span>
    <span class="abs mid opt" style="left:228px;top:106px">20kg</span>
    <span class="abs radio" style="left:304px;top:106px"></span>
    <span class="abs mid opt" style="left:348px;top:106px">10kg</span>
    <span class="abs radio" style="left:428px;top:106px"></span>
    <span class="abs mid opt" style="left:478px;top:106px">500kg</span>
  </section>

  <section class="band band--extras">
    <h2 class="abs mid group-title" style="top:58px;font-weight:400">Additional tip</h2>
    <span class="abs radio" style="left:52px;top:122px"></span>
    <span class="abs mid opt" style="left:96px;top:122px">10%</span>
    <span class="abs radio" style="left:184px;top:122px"></span>
    <span class="abs mid opt" style="left:228px;top:122px">20%</span>
    <span class="abs radio" style="left:304px;top:122px"></span>
    <span class="abs mid opt" style="left:348px;top:122px">10%</span>

    <h2 class="abs mid group-title" style="top:196px;font-weight:400">Elastic extension</h2>
    <span class="abs radio" style="left:52px;top:260px"></span>
    <span class="abs mid opt" style="left:96px;top:260px">10%</span>
    <span class="abs radio" style="left:184px;top:260px"></span>
    <span class="abs mid opt" style="left:228px;top:260px">20%</span>
  </section>

</main>
</body>
</html>
```